2024 Comprehensive Needs Assessment

Design our 2024 Binder Report Cover. Front, Spine, Back. We are in the Education field, reporting data for strategic planning. I have attached our color palette and the previous years covers as a sample.

```html
<!DOCTYPE html>
<html lang="en">
<head>
<meta charset="utf-8">
<title>2024 Comprehensive Needs Assessment – Binder Cover</title>
<link rel="stylesheet" href="https://fonts.googleapis.com/css2?family=Montserrat:wght@400;600;700;800&family=Oswald:wght@600;700&family=Tinos:wght@700&display=swap">
<style>
  :root {
    --navy: #1c4f72;
    --navy-deep: #15425f;
    --teal: #229e94;
    --teal-bright: #18c2a6;
    --ink: #0f4a62;
    --white: #ffffff;
    --stage: #e4e4e4;
  }
  * { box-sizing: border-box; margin: 0; padding: 0; }
  html, body { width: 960px; height: 1200px; overflow: hidden; background: var(--stage); }
  .canvas { position: relative; width: 960px; height: 1200px; }
  .spread {
    position: absolute; left: 40px; top: 287px;
    width: 924px; height: 657px;
    transform: scale(0.9524); transform-origin: top left;
    background: var(--navy);
    font-family: "Montserrat", sans-serif; color: var(--white);
    overflow: hidden;
  }
  .panel { position: absolute; top: 0; height: 657px; }
  .back-cover { left: 0; width: 430px; background: var(--navy); }
  .spine { left: 430px; width: 63px; background: var(--navy); border-left: 1px solid #174563; border-right: 1px solid #174563; overflow: hidden; }
  .front-cover { left: 493px; width: 431px; background: var(--navy-deep); }

  .title-stack { position: absolute; left: 64px; width: 300px; top: 64px; text-align: center; font-family: "Oswald", sans-serif; font-weight: 700; line-height: 1; }
  .title-stack .t-top { font-size: 24px; letter-spacing: 0.2px; }
  .title-stack .t-needs { font-family: "Montserrat", sans-serif; font-weight: 800; font-size: 40px; color: var(--teal-bright); letter-spacing: 2px; margin-top: 3px; }
  .title-stack .t-bottom { font-size: 30px; margin-top: 2px; }

  .summary { position: absolute; left: 27px; width: 376px; top: 212px; }
  .summary h2 { font-family: "Tinos", serif; font-weight: 700; font-size: 18px; text-align: center; letter-spacing: 0.3px; margin-bottom: 4px; }
  .summary p { font-size: 13.6px; line-height: 18px; text-align: justify; }

  .brand { display: flex; align-items: center; gap: 6px; }
  .brand .dot { width: 14px; height: 14px; border-radius: 50%; background: var(--white); flex: none; }
  .brand .name { font-weight: 700; color: var(--white); line-height: 1.1; }

  .back-brand { position: absolute; left: 55px; top: 578px; }
  .back-brand .name { font-size: 15px; }
  .back-address { position: absolute; left: 194px; width: 180px; top: 573px; text-align: center; font-weight: 700; font-size: 13px; line-height: 16.5px; font-style: normal; }

  .spine-brand { position: absolute; left: 6px; top: 28px; }
  .spine-brand .dot { width: 7px; height: 7px; }
  .spine-brand .name { font-size: 6.5px; }
  .spine-title { position: absolute; left: 22px; top: 97px; writing-mode: vertical-rl; font-weight: 800; font-size: 15px; line-height: 20px; white-space: nowrap; }
  .spine-title .accent { color: var(--teal-bright); font-weight: 700; }
  .spine-district-name { position: absolute; left: 30px; top: 460px; writing-mode: vertical-rl; white-space: nowrap; font-weight: 800; font-size: 20px; line-height: 24px; color: var(--teal-bright); letter-spacing: 1px; }
  .spine-district-sub { position: absolute; left: 12px; top: 460px; writing-mode: vertical-rl; white-space: nowrap; font-weight: 700; font-size: 11px; line-height: 16px; letter-spacing: 0.6px; }
  .spine-year { position: absolute; left: 0; width: 63px; top: 598px; text-align: center; font-family: "Oswald", sans-serif; font-weight: 700; font-size: 20px; line-height: 24px; color: var(--teal-bright); }

  .front-art { position: absolute; inset: 0; }
  .front-brand { position: absolute; left: 28px; top: 55px; }
  .front-brand .dot { width: 22px; height: 22px; }
  .front-brand .name { font-size: 22px; }

  .front-title { position: absolute; left: 105px; width: 200px; top: 414px; text-align: center; font-family: "Oswald", sans-serif; font-weight: 700; line-height: 1; }
  .front-title .t-top { font-size: 23px; }
  .front-title .t-needs { font-family: "Montserrat", sans-serif; font-weight: 800; font-size: 37px; color: var(--teal-bright); letter-spacing: 2px; margin-top: 2px; }
  .front-title .t-bottom { font-size: 28px; margin-top: 1px; }

  .district-name { position: absolute; left: 50px; width: 240px; top: 520px; text-align: center; font-weight: 800; font-size: 35px; color: var(--ink); letter-spacing: 1.5px; line-height: 1; }
  .district-sub { position: absolute; left: 50px; width: 240px; top: 557px; text-align: center; font-weight: 700; font-size: 18px; color: var(--teal); letter-spacing: 1.5px; line-height: 1; }
  .front-year { position: absolute; left: 292px; top: 532px; font-family: "Oswald", sans-serif; font-weight: 700; font-size: 49px; color: var(--teal-bright); line-height: 1; }
</style>
</head>
<body>
<main class="canvas">
  <div class="spread">

    <section class="panel back-cover">
      <div class="title-stack">
        <div class="t-top">COMPREHENSIVE</div>
        <div class="t-needs">NEEDS</div>
        <div class="t-bottom">ASSESSMENT</div>
      </div>
      <div class="summary">
        <h2>SUMMARY</h2>
        <p>Lorem ipsum dolor sit amet, consectetur adipiscing elit, sed do eiusmod tempor incididunt ut labore et dolore magna aliqua. Ut enim ad minim veniam, quis nostrud exercitation ullamco laboris nisi ut aliquip ex ea commodo consequat. Duis aute irure dolor in reprehenderit in voluptate velit esse cillum dolore eu fugiat nulla pariatur. Excepteur sint occaecat cupidatat non proident, sunt in culpa qui officia deserunt mollit anim id est laborum.</p>
      </div>
      <div class="brand back-brand">
        <span class="dot"></span>
        <span class="name">Learning<br>Pathways, LLC</span>
      </div>
      <address class="back-address">
        4512 Maple Grove Lane<br>Fairview, MS 38600<br>662-555-0148
      </address>
    </section>

    <section class="panel spine">
      <div class="brand spine-brand">
        <span class="dot"></span>
        <span class="name">Learning<br>Pathways</span>
      </div>
      <div class="spine-title">COMPREHENSIVE <span class="accent">NEEDS</span> ASSESSMENT</div>
      <div class="spine-district-name">RIVERTON</div>
      <div class="spine-district-sub">SCHOOL DISTRICT</div>
      <div class="spine-year">2024</div>
    </section>

    <section class="panel front-cover">
      <svg class="front-art" width="431" height="657" viewBox="0 0 431 657" xmlns="http://www.w3.org/2000/svg">
        <defs>
          <linearGradient id="photoTone" x1="0" y1="0" x2="0.2" y2="1">
            <stop offset="0" stop-color="#cfd8e0"/>
            <stop offset="0.55" stop-color="#a9b8c6"/>
            <stop offset="1" stop-color="#4a5e70"/>
          </linearGradient>
          <linearGradient id="titleShade" x1="0" y1="0" x2="1" y2="0">
            <stop offset="0" stop-color="#0d2a3d" stop-opacity="0"/>
            <stop offset="0.3" stop-color="#0d2a3d" stop-opacity="0.75"/>
            <stop offset="1" stop-color="#0d2a3d" stop-opacity="0.8"/>
          </linearGradient>
        </defs>
        <rect width="431" height="657" fill="url(#photoTone)" role="img" aria-label="Photo of a laptop screen showing an analytics dashboard with charts"/>
        <polygon points="0,0 300,0 0,450" fill="#1a4c6f"/>
        <polygon points="319,0 345,0 90,390 60,420" fill="#8a9fb1" opacity="0.55"/>
        <polygon points="279,0 319,0 60,420 30,440" fill="var(--teal)"/>
        <rect x="0" y="412" width="431" height="108" fill="url(#titleShade)"/>
        <polygon points="230,657 398,372 431,372 431,420 272,657" fill="var(--teal)"/>
        <polygon points="431,420 431,657 272,657" fill="#15425f"/>
        <polygon points="38,519 329,519 299,585 6,585" fill="var(--white)"/>
      </svg>
      <div class="brand front-brand">
        <span class="dot"></span>
        <span class="name">Learning<br>Pathways</span>
      </div>
      <div class="front-title">
        <div class="t-top">COMPREHENSIVE</div>
        <div class="t-needs">NEEDS</div>
        <div class="t-bottom">ASSESSMENT</div>
      </div>
      <div class="district-name">RIVERTON</div>
      <div class="district-sub">SCHOOL DISTRICT</div>
      <div class="front-year">2024</div>
    </section>

  </div>
</main>
</body>
</html>
```